Owen Tressick's Lab : Protein Folding & Directed Evolution

We would like a very streamlined website made to advertise our research lab , KVRF @ University of Coldharbor. Dr. Tressick has provided me a link of an example that he likes the simplicity and formatting of: https://www.venmarrolab.org
He would like a very similar format, especially the all in one page where you can click on various parts and be drawn to sections.
Below is the information that we would like populated into our website. Clearly the photo's and formatting need some creative work and help.
We then would like to be able to place this on our university web page. They use the format of WordPress.
Hello,
I have narrowed my choice down to 2 designers and plan to make a final choice on Monday 4-3. I have appreciated all the work done and the edits made by specific designers thus far. I especially appreciate the direct messaging that has been taking place so that I can better refine what Dr. Tressick would like in his website.
Thank you,
Marla
Target Market(s)
University students ( graduate students ) and Scientists pursuing PhD's and post doctoral candidates.
Industry/Entity Type
University Research Lab
Coding
Coded - Design and coding required
Number of Pages Required
1 page
Look and feel
Each slider illustrates characteristics of the customer's brand and the style your logo design should communicate.

```html
<!DOCTYPE html>
<html lang="en">
<head>
<meta charset="utf-8">
<title>Owen Tressick's Lab — Protein Folding &amp; Directed Evolution</title>
<link href="https://fonts.googleapis.com/css2?family=Montserrat:wght@500;700;800&family=Raleway:wght@700;800&family=Open+Sans:ital,wght@0,400;1,400&display=swap" rel="stylesheet">
<style>
:root{
  --ink:#1f1a17;
  --text:#5a5a5a;
  --heading:#262626;
  --link:#1f3fd6;
  --band:#f4f4f4;
  --white:#ffffff;
}
*{box-sizing:border-box;margin:0;padding:0}
html,body{width:1200px;height:3458px;overflow:hidden;background:var(--white)}
body{position:relative;font-family:"Open Sans",Verdana,sans-serif;color:var(--text)}
a{color:var(--link)}

.hero{position:absolute;top:0;left:0;width:1200px;height:776px;
  background:radial-gradient(ellipse 380px 260px at 330px 470px,rgba(120,90,210,.75),transparent 75%),
  radial-gradient(ellipse 300px 300px at 860px 500px,rgba(90,60,180,.8),transparent 75%),
  radial-gradient(ellipse 150px 240px at 560px 300px,rgba(95,201,214,.7),transparent 80%),
  radial-gradient(ellipse 200px 200px at 700px 220px,rgba(150,120,220,.7),transparent 80%),
  linear-gradient(180deg,#857a70 0%,#cfc7bb 25%,#e6e1d8 55%,#d3ccc6 100%)}
.nav{position:absolute;top:0;left:0;width:1200px;height:112px;display:flex;align-items:center;justify-content:space-between;padding:0 68px 0 86px}
.nav a{font-family:Montserrat,sans-serif;font-weight:500;font-size:13.5px;letter-spacing:1.2px;color:#111;text-decoration:none}
.nav .brand{font-size:25px;font-weight:700;color:var(--white);letter-spacing:1px}
.hero-title{position:absolute;top:198px;left:79px;font-family:Montserrat,sans-serif;font-weight:800;font-size:39px;line-height:60px;color:#0e0e0e;letter-spacing:.5px}

.research-title,.team-title{position:absolute;left:0;width:1200px;text-align:center;font-family:Raleway,sans-serif;font-weight:800;font-size:32px;color:var(--ink);letter-spacing:.5px}
.research-title{top:825px}
.intro{position:absolute;top:881px;left:181px;width:822px;font-size:12.2px;line-height:18.8px;letter-spacing:.3px}

.topic{position:absolute;left:0;width:1200px}
.topic .figure{position:absolute;left:205px;width:345px}
.topic .copy{position:absolute;left:599px;width:420px}
.topic h3{font-weight:400;font-size:22.5px;line-height:30px;color:var(--heading);margin-bottom:22px;letter-spacing:.3px}
.topic p{font-size:12.2px;line-height:18.8px;margin-bottom:18px;letter-spacing:.3px}

.topic--serf{top:1084px}
.topic--serf .figure{top:26px;height:294px;background:linear-gradient(135deg,#f6c9a6 0%,#f3b083 50%,#efc3a0 100%)}
.topic--spy{top:1556px}
.topic--spy .figure{top:-24px;height:268px;width:370px;background:linear-gradient(90deg,#5c9a50 0%,#d9ead3 45%,#e8f1e2 75%,#8fd14f 100%)}
.topic--nicotine{top:1906px}
.topic--nicotine .figure{top:30px;height:340px;width:360px;background:radial-gradient(circle at 50% 70%,#dcdb5a 0%,#e8e59a 45%,#ffffff 80%)}
.topic--quadruplex{top:2444px}
.topic--quadruplex .figure{top:20px;height:230px;width:350px;background:radial-gradient(ellipse at 50% 45%,#6cd646 0%,#b9d6b0 35%,#e2e2e2 60%,#ffffff 85%)}

.team{position:absolute;top:2892px;left:0;width:1200px;height:566px;background:var(--band)}
.team-title{top:66px}
.team .portrait{position:absolute;top:149px;left:268px;width:250px;height:298px;background:linear-gradient(180deg,#c9c9c9 0%,#b5b5b5 60%,#2a2a2a 100%)}
.team .profile{position:absolute;top:152px;left:548px;width:470px}
.profile h4{font-weight:400;font-size:25px;line-height:30px;color:var(--heading);letter-spacing:.5px}
.profile .role{font-style:italic;font-size:23px;line-height:31px;color:var(--heading);margin-bottom:18px}
.profile .email{font-size:12.2px;margin-bottom:14px;letter-spacing:.3px}
.profile ul{list-style:disc;padding-left:22px;font-size:12.2px;line-height:18.8px;margin-bottom:14px;letter-spacing:.3px}
.profile .bio{font-size:12.2px;line-height:18.8px;letter-spacing:.3px}
</style>
</head>
<body>

<header class="hero" role="img" aria-label="Rendered 3D protein structure in translucent purple and teal">
  <nav class="nav">
    <a href="#home">HOME</a>
    <a href="#research">RESEARCH</a>
    <a href="#team">TEAM</a>
    <a href="#home" class="brand">Owen Tressick's Lab</a>
    <a href="#publications">PUBLICATIONS</a>
    <a href="#join">JOIN</a>
    <a href="#contact">CONTACT</a>
  </nav>
  <h1 class="hero-title">Protein Folding &amp;<br>Directed Evolution</h1>
</header>

<h2 class="research-title" id="research">RESEARCH</h2>
<p class="intro">Proteins start life as linear amino acid sequences and end up as beautifully folded, active structures. Dr. Tressick's laboratory focuses on recently discovered machinery that drives protein folding in the cell. Powerful genetic, structural, and biophysical tools are being used to generate a detailed picture of how these folding machines work. Members of the Tressick lab also use directed evolution to improve protein folding. They do this by asking organisms themselves to solve difficult protein-folding problems. By examining the solutions to these problems, they are better able to understand folding in the cell.</p>

<section class="topic topic--serf">
  <div class="figure" role="img" aria-label="Diagram of a cell showing nucleus, nucleolus, RNA, SERF, condensate and amyloid"></div>
  <div class="copy">
    <h3>Studying the Physiological Function<br>of Human SERF2</h3>
    <p>Our lab has successfully discovered the development of amyloid aggregation biosensors in yeast.&nbsp; SERF has been shown to accelerate amyloid aggregation both in vitro and in vivo.&nbsp; It can modulate the disease progression of Alzheimer's and Parkinson's Disease in animal models.&nbsp; By determining the physiological functions of SERF, we aim to provide more perspectives on diseases interventions.</p>
    <p>Our studies include using techniques such as cell biology, microscopy, RNA-seq, RNAi, CRISPR knockout and knockin as well as Cross-linking immunoprecipitation.</p>
    <p><a href="#research">https://pubs.biochemjournal.org/doi/10.1021/abchembio.0c00083</a></p>
  </div>
</section>

<section class="topic topic--spy">
  <div class="figure" role="img" aria-label="Ribbon structure of the chaperone Spy in apo and substrate-bound states"></div>
  <div class="copy">
    <h3>Studying The ATP-Chaperone Spy</h3>
    <p>Our lab is interested in exploring the functional dynamics in proteins. One area of focus is on the Spy structure.&nbsp; Specifically, how it both allows client folding-while-bound and how it prevents aggregation.</p>
    <p>Varga R, Kessler VV, Lindqvist BA, van Dorne CPM, Rosetti BT, Tressick JCA. <a href="#publications">Mechanism of the small ATP-independent chaperone Spy is substrate specific</a>. Mol Commun. 2021 Feb 8;12(1):851. doi: 10.5555/m41467-021-21120-8</p>
  </div>
</section>

<section class="topic topic--nicotine">
  <div class="figure" role="img" aria-label="Workflow diagram: library of NicA2 variants transformed into bacteria and selected for growth on nicotine plates"></div>
  <div class="copy">
    <h3>Treating nicotine addiction through<br>directed evolution</h3>
    <p>Addiction to tobacco is the leading cause of preventable death in the world. We are studying an enzyme NicA2 that degrades nicotine and has been shown to have therapeutic potential when injected into nicotine addicted rats. We find that contrary to the assumption that this enzyme uses oxygen as its electron acceptor, it instead uses a newly discovered cytochrome c, CycN.&nbsp; CycN serves as the natural electron acceptor of NicA2. The inability of CycN mutants to metabolize nicotine in the presence of oxygen opens up the opportunity to select for NicA2 mutants of increased therapeutic potential that can use oxygen directly as an electron acceptor. So far, we have uncovered variants with up to a 200-fold increase in their oxygen-dependent catalytic rate.</p>
    <p>Palmore M, Ashby CT, Tressick JCA, Quell F. (2021) <a href="#publications">A cytochrome c is the natural electron acceptor for nicotine oxidoreductase</a>. Molecular Chemical Biology. 2021 January 11. https://doi.org/10.5555/m41589-020-00712-3 <a href="#publications">LitIndex</a></p>
  </div>
</section>

<section class="topic topic--quadruplex">
  <div class="figure" role="img" aria-label="Structural model of a small protein bound to a G-quadruplex"></div>
  <div class="copy">
    <h3>How Proteins Regulate Gene<br>Function By Acting on<br>G-quadruplexes</h3>
    <p>Our research focuses on elucidating the structural basis of G-quadruplex recognition by two small highly charged and partially disordered proteins.&nbsp; The studied proteins are amenable to solution NMR and preferentially bind to G-quadraplex structures in vitro and in vivo.&nbsp; By understanding how this recognition process occurs we hope to help develop a G-quadruplex binding protein-based platform for gene regulation by manipulating the structure.&nbsp; We approach our studies using biophysical, computational and cellular biology techniques.</p>
    <p>Renwick BR, Tressick JCA. <a href="#publications">SERF, a family of tiny highly conserved, highly charged proteins with enigmatic functions</a>. FMS J. 2022, doi: 10.5555/fms.16555.</p>
  </div>
</section>

<section class="team" id="team">
  <h2 class="team-title">OUR TEAM</h2>
  <div class="portrait" role="img" aria-label="Portrait photo of Dr. Owen Tressick"></div>
  <div class="profile">
    <h4>Owen C. Tressick, Ph.D.</h4>
    <p class="role">Celia R. Hartwell Collegiate Professor, MCDBKVRF Investigator</p>
    <p class="email">Email: <a href="#contact">otressick@coldharbor.edu</a></p>
    <ul>
      <li><a href="#team">Kestrel Vale Research Foundation Investigator</a></li>
      <li><a href="#team">Department of Molecular Cellular Developmental Biology</a></li>
      <li><a href="#team">Program in Cellular Molecular Biology</a></li>
      <li><a href="#team">Department of Biophysics</a></li>
    </ul>
    <p class="bio">Owen received his PhD from the University of Farrowmere in Molecular Biology. He then continued his studies in mRNA Stability at NRI, Bacterial Genetics at Halden Medical School and Protein Folding at University of Ostrelund in Germany.&nbsp; He has been working as a researcher for 24 years and has been affiliated with KVRF and the University of Coldharbor since 2005.&nbsp; In Owen's spare time he enjoys biking, kayaking, and giving tours to Natural History Museum visitors of the coral reek and octopus tanks in his office.</p>
  </div>
</section>

</body>
</html>
```